We have over 30 years of experience in various construction projects. New additions, rehab work, interior and exterior etc. We started our own company about a year ago.
I am attaching a card that I received from a client that I really like and would like to follow as a template, but I am very open to your creative approach. I am interested in my logo (which will be later used for my website) to incorporate the "M&P" or "M&P Remodeling" Please email me at mpremodeling 81@brindlemail.com or call Walt at 773-555-0182.

Industry/Entity Type

Construction

Contact Information for Business Card

M&P Remodeling and Beacon Services
2816 W Oakridge Ave
Maple Falls, WI 60706
708-555-0147 - Polish
708-555-0163 - English

Piotr Walek - Owner
Marek WAlek Jr - Construction Manager
mpremodeling81@brindlemail.com

```html
<!DOCTYPE html>
<html lang="en">
<head>
<meta charset="utf-8">
<title>M&amp;P Remodeling – Business Card</title>
<link rel="stylesheet" href="https://fonts.googleapis.com/css2?family=EB+Garamond:ital,wght@0,400;1,400&display=swap">
<style>
  :root {
    --page-bg: #ececec;
    --card-dark: #2f2f2f;
    --card-darker: #262626;
    --ink-light: #e4e4e4;
    --ink-muted: #bdbdbd;
    --skyline-top: #1c1c1c;
    --skyline-bottom: #0e0e0e;
  }
  * { box-sizing: border-box; margin: 0; padding: 0; }
  html, body {
    width: 1200px; height: 1000px; overflow: hidden;
    background: var(--page-bg);
    font-family: "EB Garamond", Georgia, serif;
  }
  .sheet { position: relative; width: 1200px; height: 1000px; }
  .card {
    position: absolute; left: 320px; width: 560px; height: 320px;
    background: radial-gradient(ellipse at 40% 30%, var(--card-dark), var(--card-darker));
    box-shadow: 0 10px 30px rgba(0,0,0,0.25);
    overflow: hidden;
  }
  .card--front { top: 140px; }
  .card--back { top: 540px; }

  .skyline {
    position: absolute; left: 0; right: 0; bottom: 0; height: 46px;
    background: linear-gradient(to bottom, var(--skyline-top), var(--skyline-bottom));
  }

  .brand {
    position: absolute; left: 40px;
    display: flex; align-items: center; gap: 14px;
    color: var(--ink-light); font-weight: 400; line-height: 1;
  }
  .brand__square { display: block; background: var(--ink-light); }
  .card--front .brand { top: 96px; font-size: 48px; }
  .card--front .brand__square { width: 22px; height: 22px; }
  .card--back .brand { top: 36px; font-size: 26px; }
  .card--back .brand__square { width: 12px; height: 12px; }

  .tagline {
    position: absolute; left: 76px; top: 162px;
    color: var(--ink-muted); font-size: 20px;
  }

  .contact {
    position: absolute; right: 34px; top: 92px; text-align: right;
    color: var(--ink-muted); font-size: 15px; line-height: 1.35;
  }
  .contact__name { color: var(--ink-light); font-size: 22px; letter-spacing: 0.5px; }
  .contact__role { font-style: italic; font-size: 17px; margin-bottom: 2px; }
  .contact__email { margin-bottom: 10px; }
</style>
</head>
<body>
<main class="sheet">
  <section class="card card--front" aria-label="Card front">
    <div class="brand"><span class="brand__square"></span>M&amp;P Remodeling</div>
    <p class="tagline">Remodeling and Beacon Services</p>
    <div class="skyline" role="img" aria-label="City skyline silhouette"></div>
  </section>

  <section class="card card--back" aria-label="Card back">
    <div class="brand"><span class="brand__square"></span>M&amp;P Remodeling</div>
    <div class="contact">
      <p class="contact__name">Marek WAlek Jr</p>
      <p class="contact__role">Construction Manager</p>
      <p class="contact__email">mpremodeling81@brindlemail.com</p>
      <p>2816 W Oakridge Ave Maple Falls, WI</p>
      <p>708-555-0147 &nbsp;Polish</p>
      <p>708-555-0163 &nbsp;English</p>
    </div>
    <div class="skyline" role="img" aria-label="City skyline silhouette"></div>
  </section>
</main>
</body>
</html>
```